Recruitment of Brindle Staffing for the UK market

I want a website for the UK market to attract businesses and companies to come to us for Philipine labour. We want an information site that gives all information on what we do and how we can recruit Philippine labour.
This is a recruitment site for companies to contact us with their requirements for skilled workers coming from the Philipines over to the UK to work.

Target Market(s)

Uk Companies and businesses who want Philipine skilled workers

Industry/Entity Type

REcruitment

Coding

Coded - Design and coding required

Number of Pages Required

5+ page

Font styles to use
Sans Serif

Colors
0054AA
0677BA
7BADD7
CADEEF
E8F1F8
0094D4
00A9DD
6FCCEA
C7EBF8
E9F6FB
EE7325
F08F49
F5BC92
FAE3D3
FDF4ED
EB3D1F
EC4F4E
F09395
F8D3D4
FCEDEE

Requirements
Must have
• Look professional and corperate with drop down menus for Home ,about, services,articles. training , contact us
Nice to have
• Look at Tovel recruitment- https://tovelrecruitment.example.co.uk/. This is my current site - https://www.brindlestaffing.example.com/
Should not have
• Cartoons or silly pictures , needs to be corperate looking

```html
<!DOCTYPE html>
<html lang="en">
<head>
<meta charset="utf-8">
<title>Brindle Staffing – Skilled Philippine Workers for UK Companies</title>
<link rel="stylesheet" href="https://fonts.googleapis.com/css2?family=Poppins:wght@300;400;500;600&display=swap">
<style>
:root{
  --blue-dark:#0054AA;
  --blue:#0677BA;
  --blue-mid:#0094D4;
  --blue-pale:#E8F1F8;
  --orange:#EE7325;
  --red:#EB3D1F;
  --ink:#1d1d1f;
  --body:#555;
  --footer:#0d0d0f;
  --white:#fff;
}
*{box-sizing:border-box;margin:0;padding:0}
html,body{width:1200px;height:4144px;overflow:hidden}
body{font-family:'Poppins',sans-serif;color:var(--ink);background:var(--white);position:relative}
a{color:inherit;text-decoration:none}
.wrap{position:absolute;left:60px;width:1080px}

/* top bar */
.topbar{position:absolute;top:0;left:0;width:1200px;height:32px;background:var(--blue);color:#fff;font-size:15px;display:flex;justify-content:flex-end;align-items:center;gap:22px;padding-right:66px}
.topbar span{display:flex;align-items:center;gap:8px}
.topbar .phone{font-weight:600}

/* header */
.header{position:absolute;top:32px;left:0;width:1200px;height:80px;background:#fff;display:flex;align-items:center;justify-content:space-between;padding:0 62px 0 70px}
.brand{font-size:26px;font-weight:600;color:var(--blue-dark)}
.nav{display:flex;gap:38px;font-size:12px;font-weight:500;text-transform:uppercase}
.nav .active{color:var(--red)}

/* hero */
.hero{position:absolute;top:112px;left:0;width:1200px;height:585px;background:linear-gradient(90deg,#0a2f6a 0%,#1c4b82 42%,#6b6f78 70%,#8a7a62 100%)}
.hero-text{position:absolute;left:61px;top:132px;width:680px;color:#fff}
.hero h1{font-size:52px;font-weight:500;line-height:64px}
.hero p{font-size:12px;line-height:22px;margin-top:14px;width:640px}
.btn{display:inline-flex;align-items:center;gap:14px;background:var(--red);color:#fff;font-size:13px;border-radius:6px;padding:0 10px 0 18px;height:36px}
.btn i{width:22px;height:22px;border-radius:50%;background:#fff;display:flex;align-items:center;justify-content:center}
.hero .btn{margin-top:26px}

/* services */
.section-title{text-align:center;font-weight:500;font-size:42px;line-height:52px}
.sectors{top:926px;display:flex;gap:20px}
.sector{width:200px;height:225px;border-radius:6px;background:var(--blue);color:#fff;display:flex;flex-direction:column;align-items:center;justify-content:center;font-size:18px;text-align:center;line-height:28px;gap:18px}
.sector.alt{background:var(--red)}

/* working together */
.together{position:absolute;top:1254px;left:0;width:1200px;height:753px}
.together svg.band{position:absolute;top:0;left:0}
.together-intro{position:absolute;top:1398px;left:0;width:1200px;text-align:center;font-size:18px;line-height:30px;color:#444}
.steps{top:1486px;display:flex;gap:24px}
.step{width:252px;height:416px;background:#fff}
.photo{display:block}
.step .photo{height:202px}
.step-body{padding:20px 16px}
.step h3{font-size:18px;font-weight:500}
.step p{font-size:12px;line-height:22px;color:var(--body);margin-top:6px;height:110px}
.more{font-size:13px;color:var(--red);display:inline-flex;align-items:center;gap:6px}

/* articles */
.articles{top:2152px;display:flex;gap:30px}
.article{width:340px;height:421px;background:#fff;box-shadow:0 2px 10px rgba(0,0,0,.08)}
.article .photo{height:225px}
.article-body{padding:16px 20px}
.date{font-size:12px;color:#333;display:flex;align-items:center;gap:8px}
.article h3{font-size:18px;font-weight:500;line-height:26px;margin-top:10px}
.article p{font-size:12px;line-height:22px;color:var(--body);margin:8px 0 10px}

/* city band */
.cityband{position:absolute;top:2650px;left:0;width:1200px;height:526px;background:linear-gradient(180deg,#4d6a90 0%,#24344e 55%,#141c2a 100%)}
.cityband h2{position:absolute;top:100px;width:1200px;text-align:center;color:#fff;font-size:42px;font-weight:500;line-height:52px}
.tiles{top:2890px;display:flex;gap:18px}
.tile{width:348px;height:201px;color:#fff;display:flex;flex-direction:column;align-items:center;justify-content:center;gap:18px;font-size:20px}
.tile.b{background:var(--blue)}.tile.o{background:var(--orange)}.tile.r{background:var(--red)}

/* about */
.about-grid{position:absolute;top:3237px;left:60px;width:493px;height:450px;display:grid;grid-template-columns:1fr 1fr;gap:4px;border-radius:16px;overflow:hidden}
.about-text{position:absolute;top:3298px;left:616px;width:520px}
.about-text h2{font-size:38px;font-weight:500}
.about-text p{font-size:12px;line-height:22px;color:var(--body);margin-top:14px}
.about-text .btn{margin-top:30px}

/* footer */
.footer{position:absolute;top:3763px;left:0;width:1200px;height:381px}
.footer svg.curve{position:absolute;top:0;left:0}
.fcol{position:absolute;top:121px;color:#fff;font-size:12px;line-height:20px}
.fbrand{display:inline-block;background:#fff;color:var(--blue-dark);font-size:20px;font-weight:600;padding:8px 16px;margin-bottom:14px}
.fcol h4{font-size:13px;font-weight:500;margin:12px 0 22px}
.fline{display:flex;gap:12px;margin-bottom:12px;align-items:flex-start}
.news{display:flex;width:340px;height:36px;border:1px solid #fff;border-radius:18px;overflow:hidden}
.news span{flex:1;padding:0 20px;line-height:34px;font-size:12px}
.news b{background:var(--red);font-weight:400;padding:0 24px;line-height:34px;font-size:12px}
.social{display:flex;gap:10px;margin-top:16px}
.social i{width:30px;height:30px;border-radius:50%;background:#fff}
.social i.hot{background:var(--red)}
.copy{position:absolute;bottom:6px;width:1200px;text-align:center;color:#ccc;font-size:11px}
</style>
</head>
<body>

<div class="topbar">
  <span class="phone"><svg width="18" height="18" viewBox="0 0 24 24" fill="#fff"><path d="M6.6 10.8a15 15 0 0 0 6.6 6.6l2.2-2.2c.3-.3.7-.4 1-.2 1.1.4 2.3.6 3.6.6.6 0 1 .4 1 1V20c0 .6-.4 1-1 1C10.6 21 3 13.4 3 4c0-.6.4-1 1-1h3.5c.6 0 1 .4 1 1 0 1.3.2 2.5.6 3.6.1.3 0 .7-.2 1z"/></svg>07700 900123</span>
  <span><svg width="20" height="16" viewBox="0 0 20 16" fill="#fff"><path d="M0 0h20v16H0z"/><path d="M1 1l9 7 9-7" stroke="#0677BA" stroke-width="1.6" fill="none"/></svg>sales@brindlestaffing.example.com</span>
</div>

<header class="header">
  <div class="brand">Brindle Staffing</div>
  <nav class="nav">
    <a class="active">Home</a><a>About</a><a>Services</a><a>Articles</a><a>Training</a><a>Contact Us</a>
  </nav>
</header>

<section class="hero" role="img" aria-label="Engineer in a hi-vis vest working on a laptop in a workshop, with a blue overlay">
  <div class="hero-text">
    <h1>Recruiting and placing skilled Philippine workers into UK companies</h1>
    <p>Lorem Ipsum is simply dummy text of the printing and typesetting industry. Lorem Ipsum has been the industry's standard dummy text.</p>
    <a class="btn">Request A Free Quote <i><svg width="10" height="10" viewBox="0 0 10 10"><path d="M3 1l4 4-4 4" stroke="#EB3D1F" stroke-width="1.8" fill="none"/></svg></i></a>
  </div>
</section>

<h2 class="section-title" style="position:absolute;top:786px;width:1200px">A World-class<br>Recruitment Agency</h2>

<div class="wrap sectors">
  <div class="sector"><svg width="64" height="64" viewBox="0 0 64 64" fill="none" stroke="#fff" stroke-width="2.4"><circle cx="24" cy="26" r="10"/><path d="M12 22h24M8 56c0-10 7-16 16-16s16 6 16 16"/><circle cx="46" cy="44" r="8"/><path d="M46 32v4M46 52v4M34 44h4M54 44h4"/></svg>Engineer</div>
  <div class="sector alt"><svg width="64" height="64" viewBox="0 0 64 64" fill="none" stroke="#fff" stroke-width="2.4"><circle cx="32" cy="22" r="10"/><path d="M22 14h20M14 58c0-12 8-18 18-18s18 6 18 18"/><path d="M32 44v10M27 49h10"/></svg>Medical<br>Workers</div>
  <div class="sector"><svg width="64" height="64" viewBox="0 0 64 64" fill="none" stroke="#fff" stroke-width="2.4"><rect x="8" y="10" width="14" height="46"/><circle cx="40" cy="20" r="7"/><path d="M30 56V36h20v20M50 40l8-8"/></svg>Welders</div>
  <div class="sector"><svg width="64" height="64" viewBox="0 0 64 64" fill="none" stroke="#fff" stroke-width="2.4"><path d="M18 36a10 10 0 0 1 4-19 12 12 0 0 1 20 0 10 10 0 0 1 4 19v14H18z"/><path d="M18 44h28"/></svg>Chef</div>
  <div class="sector"><svg width="64" height="64" viewBox="0 0 64 64" fill="none" stroke="#fff" stroke-width="2.4"><circle cx="18" cy="46" r="10"/><circle cx="50" cy="50" r="6"/><path d="M28 46h16M10 36V22h22v14M32 28h18v16"/></svg>Agriculture</div>
</div>

<section class="together">
  <svg class="band" width="1200" height="753" viewBox="0 0 1200 753"><path d="M0 120 Q600 -120 1200 120 V753 H0z" fill="#E8F1F8"/></svg>
</section>
<h2 class="section-title" style="position:absolute;top:1316px;width:1200px">Working Together</h2>
<p class="together-intro">We recruit the finest talent available with our dedicated<br>200 strong team.</p>

<div class="wrap steps">
  <article class="step">
    <div class="photo" role="img" aria-label="Business people shaking hands across an office desk" style="background:linear-gradient(135deg,#d9d9d6,#8d8d8a)"></div>
    <div class="step-body"><h3>What We Do</h3><p>Our company has been established in the Philippines for over 20 years. We have mainly been recruiting philippine...</p><a class="more">Learn more →</a></div>
  </article>
  <article class="step">
    <div class="photo" role="img" aria-label="Two engineers in hard hats shaking hands on a city building site" style="background:linear-gradient(135deg,#b9c9d8,#5f7a94)"></div>
    <div class="step-body"><h3>How We Help You</h3><p>We work with companies to find skilled workers that meet the UK requirements for Visas and work permits. We guide you through...</p><a class="more">Learn more →</a></div>
  </article>
  <article class="step">
    <div class="photo" role="img" aria-label="Three workers in orange safety vests and hard hats in a factory" style="background:linear-gradient(135deg,#6e6a64,#c2702f)"></div>
    <div class="step-body"><h3>Where to start</h3><p>We need to know what your issues are and how we can understand the personnal you require , over what time frame...</p><a class="more">Learn more →</a></div>
  </article>
  <article class="step">
    <div class="photo" role="img" aria-label="Smiling support agent with a headset working at a laptop" style="background:linear-gradient(135deg,#e6e2dc,#9b8a78)"></div>
    <div class="step-body"><h3>Contact us today</h3><p>Please contact us today with your requirements , this can be care workers ,chef, welders, pipe fitters, caravan cabinet makers, medical workers.</p><a class="more">Learn more →</a></div>
  </article>
</div>

<h2 class="section-title" style="position:absolute;top:2072px;width:1200px">Our Recent Articles</h2>

<div class="wrap articles">
  <article class="article">
    <div class="photo" role="img" aria-label="Construction engineers reviewing plans beside a high-rise building" style="background:linear-gradient(135deg,#c6ccd3,#d99a4a)"></div>
    <div class="article-body"><div class="date"><svg width="16" height="16" viewBox="0 0 16 16" fill="none" stroke="#EB3D1F" stroke-width="1.4"><rect x="1.5" y="3" width="13" height="11.5"/><path d="M1.5 6.5h13M5 1v3M11 1v3"/></svg>April 20, 2022</div><h3>Lorem Ipsum is simply dummy text of the printing.</h3><p>Lorem Ipsum is simply dummy text of the printing and typesetting industry.</p><a class="more">Learn more →</a></div>
  </article>
  <article class="article">
    <div class="photo" role="img" aria-label="Chef in whites preparing food in a professional kitchen" style="background:linear-gradient(135deg,#d7dbd6,#8c9487)"></div>
    <div class="article-body"><div class="date"><svg width="16" height="16" viewBox="0 0 16 16" fill="none" stroke="#EB3D1F" stroke-width="1.4"><rect x="1.5" y="3" width="13" height="11.5"/><path d="M1.5 6.5h13M5 1v3M11 1v3"/></svg>April 20, 2022</div><h3>Lorem Ipsum is simply dummy text of the printing.</h3><p>Lorem Ipsum is simply dummy text of the printing and typesetting industry.</p><a class="more">Learn more →</a></div>
  </article>
  <article class="article">
    <div class="photo" role="img" aria-label="Doctor with a stethoscope examining an elderly patient" style="background:linear-gradient(135deg,#eef0f2,#b4bcc6)"></div>
    <div class="article-body"><div class="date"><svg width="16" height="16" viewBox="0 0 16 16" fill="none" stroke="#EB3D1F" stroke-width="1.4"><rect x="1.5" y="3" width="13" height="11.5"/><path d="M1.5 6.5h13M5 1v3M11 1v3"/></svg>April 20, 2022</div><h3>Lorem Ipsum is simply dummy text of the printing.</h3><p>Lorem Ipsum is simply dummy text of the printing and typesetting industry.</p><a class="more">Learn more →</a></div>
  </article>
</div>

<section class="cityband" role="img" aria-label="City skyline at dusk">
  <h2>We help you find the right people<br>for your business</h2>
</section>
<div class="wrap tiles">
  <div class="tile b"><svg width="64" height="56" viewBox="0 0 64 56" fill="none" stroke="#fff" stroke-width="2.4"><circle cx="18" cy="14" r="8"/><path d="M4 54c0-12 6-20 14-20s14 8 14 20"/><path d="M36 8h24M36 18h24M36 28h24M40 38h20"/></svg>UK Skilled Workers List</div>
  <div class="tile o"><svg width="44" height="60" viewBox="0 0 44 60" fill="none" stroke="#fff" stroke-width="2.4"><rect x="2" y="2" width="40" height="56"/><path d="M10 12h24M10 20h24M10 28h24"/><circle cx="22" cy="44" r="6"/></svg>Sponsor Licence</div>
  <div class="tile r"><svg width="60" height="60" viewBox="0 0 60 60" fill="none" stroke="#fff" stroke-width="2.4"><rect x="14" y="4" width="40" height="52"/><path d="M24 14h22M24 22h22"/><circle cx="18" cy="38" r="12"/><path d="M26 46l8 8"/></svg>Recruitment Timeline</div>
</div>

<div class="about-grid">
  <div role="img" aria-label="Engineers in hard hats on a construction site" style="background:linear-gradient(135deg,#aeb7bf,#d99a3a)"></div>
  <div role="img" aria-label="Medical team in white coats" style="background:linear-gradient(135deg,#dfe6ee,#8fa7c1)"></div>
  <div role="img" aria-label="Care worker greeting an elderly man" style="background:linear-gradient(135deg,#cfd5dc,#7c8a99)"></div>
  <div role="img" aria-label="Welder in a mask at work in a workshop" style="background:linear-gradient(135deg,#5b5d61,#23262b)"></div>
</div>
<div class="about-text">
  <h2>What the business is about</h2>
  <p>We source skilled workers directly from the Philippines to work in the UK. With offices , training locations and specialist recruiters we can find the highest quality individuals to add value and resources to any UK business. We delivery quality based on vast experience over a number of years.</p>
  <p>Lorem Ipsum is simply dummy text of the printing and typesetting industry. Lorem Ipsum has been the industry's standard dummy text ever since the 1500s, when an unknown printer took a galley of type and scrambled it to make a type specimen book.</p>
  <a class="btn">Contact Us Today <i><svg width="10" height="10" viewBox="0 0 10 10"><path d="M3 1l4 4-4 4" stroke="#EB3D1F" stroke-width="1.8" fill="none"/></svg></i></a>
</div>

<footer class="footer">
  <svg class="curve" width="1200" height="381" viewBox="0 0 1200 381"><path d="M0 110 Q600 -110 1200 110 V381 H0z" fill="#0d0d0f"/></svg>
  <div class="fcol" style="left:61px;top:122px;width:290px">
    <div class="fbrand">Brindle Staffing</div>
    <p>We source skilled workers directly from the Philippines to work in the UK. With offices , training locations and specialist recruiters we can find the highest quality individuals to add value and resources to any UK business.</p>
  </div>
  <div class="fcol" style="left:428px;width:310px">
    <h4>Contact Us</h4>
    <div class="fline"><svg width="14" height="18" viewBox="0 0 14 18" fill="none" stroke="#EB3D1F" stroke-width="1.6"><path d="M7 17s6-6 6-10A6 6 0 0 0 1 7c0 4 6 10 6 10z"/><circle cx="7" cy="7" r="2"/></svg><span>Larkspur Gardens, Seaford Seaford SF18 1<br>United Kingdom</span></div>
    <div class="fline"><svg width="16" height="16" viewBox="0 0 24 24" fill="none" stroke="#EB3D1F" stroke-width="2"><path d="M6.6 10.8a15 15 0 0 0 6.6 6.6l2.2-2.2c.3-.3.7-.4 1-.2 1.1.4 2.3.6 3.6.6.6 0 1 .4 1 1V20c0 .6-.4 1-1 1C10.6 21 3 13.4 3 4c0-.6.4-1 1-1h3.5c.6 0 1 .4 1 1 0 1.3.2 2.5.6 3.6.1.3 0 .7-.2 1z"/></svg><b style="font-weight:500">07700 900123</b></div>
    <div class="fline"><svg width="18" height="14" viewBox="0 0 18 14" fill="none" stroke="#EB3D1F" stroke-width="1.6"><rect x="1" y="1" width="16" height="12"/><path d="M1 1l8 6 8-6"/></svg><span>sales@brindlestaffing.example.com</span></div>
  </div>
  <div class="fcol" style="left:801px;width:340px">
    <h4>Subscribe To Our Newsletter:</h4>
    <div class="news"><span>E-mail*</span><b>Subscribe</b></div>
    <div class="social"><i></i><i></i><i class="hot"></i><i></i></div>
  </div>
  <p class="copy">© 2023 All Rights Reserved | Brindle Staffing Ltd</p>
</footer>

</body>
</html>
```